Breezeway Comfort business cards design

Need a business card design for a Heating and Air Conditioning business. I need these items included.
Business name: Breezeway Comfort
Owner: Marcus Tollefsen
License # 2874590
Phone number # 555-382-4071
Email: breezewaycomfortair@mailvista.example
Sales
Service
Installation
Maintenance

Heating and Air Conditioning

Requirements
Must have
• Company name , license number , phone number , email

```html
<!DOCTYPE html>
<html lang="en">
<head>
<meta charset="utf-8">
<title>Breezeway Comfort – Business Cards</title>
<link rel="stylesheet" href="https://fonts.googleapis.com/css2?family=Montserrat:wght@400;500;700&family=Oswald:wght@600&display=swap">
<style>
  :root {
    --backdrop: #e6e7ea;
    --card-white: #ffffff;
    --ink: #1d1d22;
    --brand-orange: #f47a2c;
    --band-start: #ef5a4b;
    --band-end: #fb9a2a;
    --brand-blue: #1f45b8;
    --back-blue-light: #1f4fc6;
    --back-blue-dark: #0c2f9b;
  }
  * { margin: 0; padding: 0; box-sizing: border-box; }
  html, body { width: 1200px; height: 1200px; overflow: hidden; }
  body {
    background: var(--backdrop);
    font-family: "Montserrat", Arial, sans-serif;
    position: relative;
  }
  .card {
    position: absolute;
    left: 150px;
    width: 900px;
    height: 514px;
    border-radius: 32px;
    overflow: hidden;
    border-bottom: 5px solid var(--brand-orange);
    box-shadow: 0 10px 28px rgba(0,0,0,0.18);
  }
  .card--front { top: 64px; background: var(--card-white); }
  .card--back {
    top: 620px;
    background: linear-gradient(135deg, var(--back-blue-light), var(--back-blue-dark));
    display: flex; align-items: center; justify-content: center;
  }

  .contact { position: absolute; left: 70px; top: 150px; }
  .contact__name {
    color: var(--brand-orange);
    font-weight: 700;
    font-size: 44px;
    letter-spacing: 0.5px;
    line-height: 1;
  }
  .contact__role {
    color: var(--ink);
    font-weight: 500;
    font-size: 26px;
    margin-top: 4px;
    margin-bottom: 18px;
  }
  .contact__line {
    display: flex; align-items: center; gap: 12px;
    color: var(--ink);
    font-size: 24px;
    font-weight: 400;
    margin-bottom: 10px;
  }
  .contact__icon { width: 28px; height: 28px; flex: none; }
  .contact__line--plain { padding-left: 40px; }

  .brand {
    position: absolute; right: 60px; top: 34px;
    display: flex; align-items: center; gap: 16px;
  }
  .brand__dot { width: 34px; height: 34px; border-radius: 50%; background: var(--brand-orange); }
  .brand__name {
    color: var(--brand-blue);
    font-weight: 700;
    font-size: 46px;
    line-height: 1.05;
    letter-spacing: 1px;
    text-transform: uppercase;
  }

  .services {
    position: absolute; left: 0; right: 0; top: 392px; height: 52px;
    background: linear-gradient(90deg, var(--band-start), var(--band-end));
    display: flex; align-items: center; justify-content: center; gap: 18px;
    font-family: "Oswald", "Arial Narrow", sans-serif;
    font-weight: 600;
    font-size: 28px;
    color: #ffffff;
    letter-spacing: 1px;
    text-transform: uppercase;
  }
  .services__sep { font-size: 18px; }

  .back-brand { display: flex; align-items: center; gap: 18px; }
  .back-brand__dot { width: 40px; height: 40px; border-radius: 50%; background: var(--brand-orange); }
  .back-brand__name {
    color: #ffffff;
    font-weight: 700;
    font-size: 52px;
    letter-spacing: 1px;
    text-transform: uppercase;
    line-height: 1.05;
  }
</style>
</head>
<body>
  <section class="card card--front">
    <div class="brand">
      <span class="brand__dot"></span>
      <p class="brand__name">Breezeway<br>Comfort</p>
    </div>

    <div class="contact">
      <p class="contact__name">MARCUS TOLLEFSEN</p>
      <p class="contact__role">OWNER</p>
      <p class="contact__line">
        <svg class="contact__icon" viewBox="0 0 24 24" aria-hidden="true"><path fill="#f47a2c" d="M6.6 10.8a15.1 15.1 0 0 0 6.6 6.6l2.2-2.2c.3-.3.7-.4 1-.2 1.1.4 2.3.6 3.6.6.6 0 1 .4 1 1V20c0 .6-.4 1-1 1A17 17 0 0 1 3 4c0-.6.4-1 1-1h3.5c.6 0 1 .4 1 1 0 1.3.2 2.5.6 3.6.1.3 0 .7-.2 1z"/></svg>
        555-382-4071
      </p>
      <p class="contact__line">
        <svg class="contact__icon" viewBox="0 0 24 24" aria-hidden="true"><rect x="2" y="5" width="20" height="14" rx="1.5" fill="#f47a2c"/><path d="M3 6.5l9 6.5 9-6.5" fill="none" stroke="#fff" stroke-width="1.6"/></svg>
        breezewaycomfortair@mailvista.example
      </p>
      <p class="contact__line contact__line--plain">License #2874590</p>
    </div>

    <div class="services">
      <span>Sales</span><span class="services__sep">●</span>
      <span>Service</span><span class="services__sep">●</span>
      <span>Installation</span><span class="services__sep">●</span>
      <span>Maintenance</span>
    </div>
  </section>

  <section class="card card--back">
    <div class="back-brand">
      <span class="back-brand__dot"></span>
      <p class="back-brand__name">Breezeway<br>Comfort</p>
    </div>
  </section>
</body>
</html>
```